Women's Empowerment & Prayer Brunch - Matching Poster, flyer and Postcard

We are a Christian Event & Travel Company and we are hosting our inaugural event on June 10, 2017. This event is a women's empowerment & prayer brunch aboard a private yacht leaving out of Larkspur Landing, Maryland. The event will cater to women who have a vision to start or have already embarked on the journey of starting or growing a business or ministry. The event calls for a matching poster, flyer and postcard design that give an elegant & exquisite feel with just the right breath of freshness. The colors should reflect our logo as this is our launch event. I have also included 2 photos of the Coralwind Heritage Village production (one of our sponsors) - Please include but do not make it take over the design - this is to advertise the door prize. The final design will portray the branding of the company (Christian, travel, events, elegance, professional), the branding of the event (elegant and luxurious) and the importance of this launch event.
Please include the following information:
Brightwell Event & Travel Group presents
Event name: Climbing the Hill: Trust, Service & Devotion.
Tag Line/Description: An Exquisite Women's Empowerment & Prayer Brunch.
Guest Speaker: Minister Harriet L. Dunmore (Photo included)
VP of TrustLine
Asst. Pastor & First Lady of Gilead Baptist Church
Special Guest Psalmist: Minister Tessa Holbrook (Photo Included)
Worship Director of Stonefield Community Church
Vocalist, Songwriter, Musician, and Clinician
Venue: Aboard the Regal Tide Yacht
Dock: Larkspur Landing
342 Marlow Court, Oxen Hill, MD 20712
Boarding 10:00am
Sailing Promptly at 10:30am
(Please be on time the yacht will not wait)
Date: Saturday June 10, 2017
Tickets: Early Bird US$75.00/person (ends May 15, 2017)
Regular Tickets US$95.99
Purchase Tickets at www.brightwellevent-travel.example/climbing-the-hill
SPACE IS LIMITED DUE TO YACHT CAPACITY
Grand Prize: Julian Ardent Purse
Door Prize: 2 Tickets to the Islander Coralwind Heritage Village
Other prizes for special ladies in attendance.
Ladies are asked to dress in Elegant White Ensemble
Corporate Sponsors:
The Coralwind Heritage Village (Logo included)
R. Lanning Photography (Logo included)
Special Thanks to our Individual Sponsors:
Mrs. G. Whitlow, Mr. K Prentice & Mr. S. Dorsey

Target Market(s)

Women, Business, Ministry, Christians, Middle to Upper Class

Industry/Entity Type

Events

Font styles to use
Serif
Script

Requirements
Must have
• Elegance, professional, vivid in color & font. be creative in Visual and FONT!
• Poster: 18" X 24"
• Flyer: one sided.
• ***** the final design chosen will have a cross referenced design of 1 flyer, 1 postcard 1 poster. This was included so you have a reference - Be creative!!!!!!
Nice to have
• Matching across all 3 designs (poster, flyer & postcard) but sized appropriately and just enough difference to play up the design and be appealing.
• I uploaded 3 example flyers to give you inspiration of the type of visuals I'm looking for. I removed my amateur sample because the designs were copying it instead of being creative.
Should not have
• Any thing inappropriate, alcohol oriented or sexual

```html
<!DOCTYPE html>
<html lang="en">
<head>
<meta charset="utf-8">
<title>Climbing the Hill – Women's Empowerment & Prayer Brunch</title>
<link rel="stylesheet" href="https://fonts.googleapis.com/css2?family=Cinzel:wght@500;700&family=Great+Vibes&family=Roboto:wght@400;500&family=Roboto+Condensed:wght@500;700&family=Oswald:wght@600&display=swap">
<style>
:root{
  --ink:#050505;
  --gold:#f3b53a;
  --gold-deep:#b87a12;
  --gold-light:#ffe28a;
  --sky:#8fd0ec;
  --magenta:#e35ae8;
  --lemon:#f7ea6a;
  --navy:#1c2a6e;
  --cream:#f4e6c4;
  --paper:#ffffff;
  --tab:#f5b82a;
  --violet:#7a1a8a;
}
*{margin:0;padding:0;box-sizing:border-box}
html,body{width:900px;height:1200px;overflow:hidden;background:var(--ink)}
.poster{position:relative;width:900px;height:1200px;overflow:hidden;background:var(--ink);font-family:"Roboto",sans-serif;color:#fff}
.abs{position:absolute}
.text{z-index:3;white-space:nowrap}

.title{left:0;width:900px;top:34px;text-align:center;font-family:"Cinzel",serif;font-weight:700;font-size:76px;letter-spacing:1px;
  background:linear-gradient(180deg,var(--gold-light) 10%,var(--gold) 50%,var(--gold-deep) 90%);-webkit-background-clip:text;background-clip:text;color:transparent}
.subtitle{left:0;width:900px;top:116px;text-align:center;font-family:"Great Vibes",cursive;font-size:84px;line-height:1.1;color:var(--sky)}

.hero-glow{left:0;top:230px;width:560px;height:295px;background:radial-gradient(ellipse at 40% 45%,#b3162a 0%,#5a0a20 45%,rgba(5,5,5,0) 75%)}
.hero-photo{left:82px;top:242px;width:360px;height:281px;background:linear-gradient(160deg,#6b4536 0%,#c23030 55%,#3a1212 100%);border-radius:4px}

.brand-box{left:583px;top:262px;width:212px;height:144px;background:var(--navy);display:flex;align-items:center;justify-content:center;gap:10px;padding:0 14px}
.brand-dot{width:14px;height:14px;border-radius:50%;background:var(--gold);flex:none}
.brand-name{font-family:"Cinzel",serif;font-weight:500;font-size:17px;line-height:1.3;color:var(--gold);text-align:center}
.tagline{left:480px;width:410px;top:414px;text-align:center;font-family:"Cinzel",serif;font-weight:500;font-size:21px;line-height:27px;color:var(--cream)}

.photo-fire{left:527px;top:525px;width:373px;height:200px;background:linear-gradient(135deg,#1a1a1a 0%,#5a2a0a 45%,#e07a1c 60%,#2a1a10 100%);z-index:1}
.speaker{left:31px;top:558px;font-size:21px;color:var(--magenta)}
.speaker-role{left:27px;top:587px;font-size:14px;color:var(--magenta)}
.psalmist{left:90px;top:624px;font-size:19px;color:var(--lemon)}
.psalmist-role{left:70px;top:652px;width:410px;text-align:center;font-size:13px;line-height:19px;color:var(--lemon);white-space:normal}

.band{left:0;top:707px;width:900px;height:313px;z-index:0}
.photo-dance{left:600px;top:733px;width:300px;height:285px;background:linear-gradient(160deg,#1f2c1a 0%,#6a5a30 40%,#c9a85a 65%,#3f4a1f 100%);z-index:1}
.venue{left:0;width:580px;top:730px;text-align:center;font-size:17px;line-height:25px;color:#e6d4e8}
.times{left:0;width:580px;top:786px;text-align:center;font-size:19px;color:#e6d4e8}
.note{left:0;width:580px;top:813px;text-align:center;font-size:14px;color:#e6d4e8}
.date{left:25px;top:846px;font-family:"Oswald",sans-serif;font-weight:600;font-size:52px;color:var(--gold);letter-spacing:1px}
.tickets{left:25px;top:917px;font-family:"Roboto Condensed",sans-serif;font-weight:700;font-size:19px;line-height:32px;color:#fff}
.tickets .hl{color:var(--gold)}
.tickets .url{font-size:18px}
.arrow{left:480px;top:900px;width:200px;height:200px;z-index:4}

.footer{left:0;top:1020px;width:900px;height:180px;background:var(--paper);z-index:2}
.sponsor-tab{left:711px;top:1018px;width:189px;height:21px;background:var(--ink);font-size:13px;font-weight:500;line-height:21px;color:#fff;padding-left:22px;clip-path:polygon(8% 0,100% 0,100% 100%,0 100%);z-index:3}
.limited{left:26px;top:1040px;font-family:"Roboto Condensed",sans-serif;font-weight:500;font-size:21px;color:#111}
.prize-tab{left:0;width:145px;height:24px;background:var(--tab);font-family:"Roboto Condensed",sans-serif;font-weight:700;font-size:17px;line-height:24px;color:#111;padding-left:25px;clip-path:polygon(0 0,92% 0,100% 50%,92% 100%,0 100%);z-index:3}
.prize-text{left:158px;font-family:"Roboto Condensed",sans-serif;font-weight:700;font-size:17px;line-height:24px;color:#111}
.extra{left:26px;top:1134px;font-size:16px;line-height:25px;color:#222}
.extra .script{font-family:"Great Vibes",cursive;font-size:22px}
.sponsor-photo{left:608px;top:1063px;width:96px;height:68px;background:#e8e6e4;display:flex;align-items:center;justify-content:center;text-align:center;font-size:10px;line-height:13px;color:#555;padding:4px;z-index:3}
.sponsor-village{left:716px;top:1077px;width:180px;display:flex;align-items:center;gap:7px;font-size:14px;font-weight:500;line-height:17px;color:var(--gold-deep);z-index:3}
.sponsor-village .mark{width:14px;height:14px;background:var(--gold);flex:none}
.thanks{left:610px;top:1143px;font-size:13px;line-height:19px;color:#111}
</style>
</head>
<body>
<main class="poster">
  <h1 class="abs text title">Climbing the Hill</h1>
  <p class="abs text subtitle">Trust, Service &amp; Devotion.</p>

  <div class="abs hero-glow"></div>
  <div class="abs hero-photo" role="img" aria-label="Portraits of the guest speaker and the special guest psalmist"></div>

  <div class="abs brand-box">
    <span class="brand-dot"></span>
    <span class="brand-name">Brightwell Event &amp; Travel Group</span>
  </div>
  <p class="abs text tagline">An Exquisite Women's<br>Empowerment &amp; Prayer Brunch.</p>

  <div class="abs photo-fire" role="img" aria-label="Fire knife dancers spinning flaming rings at night"></div>
  <p class="abs text speaker">Guest Speaker: Minister Harriet L. Dunmore</p>
  <p class="abs text speaker-role">VP of TrustLine, Asst. Pastor &amp; First Lady of Gilead Baptist Church</p>
  <p class="abs text psalmist">Special Guest Psalmist: Minister Tessa Holbrook</p>
  <p class="abs text psalmist-role">Worship Director of Stonefield Community Church Vocalist,<br>Songwriter, Musician, and Clinician</p>

  <svg class="abs band" viewBox="0 0 900 313" aria-hidden="true">
    <defs>
      <linearGradient id="bandFill" x1="0" y1="0" x2="0" y2="1">
        <stop offset="0" stop-color="#5a1060"/>
        <stop offset="1" stop-color="#2a0530"/>
      </linearGradient>
    </defs>
    <polygon points="0,0 575,0 620,20 620,313 0,313" fill="url(#bandFill)"/>
    <polygon points="0,0 575,0 600,10 0,10" fill="#8a2a90"/>
  </svg>
  <div class="abs photo-dance" role="img" aria-label="Island dancers in grass skirts performing on stage"></div>

  <p class="abs text venue">Venue: Aboard the Regal Tide Yacht<br>Dock: Larkspur Landing, 342 Marlow Court, Oxen Hill, MD 20712</p>
  <p class="abs text times">Boarding 10:00am | Sailing Promptly at 10:30am</p>
  <p class="abs text note">(Please be on time the yacht will not wait)</p>
  <p class="abs text date">SATURDAY JUNE 10, 2017</p>
  <p class="abs text tickets">
    Tickets : Early Bird <span class="hl">US$75.00/person</span> (ends May 15, 2017)<br>
    Regular Tickets <span class="hl">US$95.99</span><br>
    <span class="url">Purchase Tickets at <span class="hl">www.brightwellevent-travel.example/climbing-the-hill</span></span>
  </p>

  <div class="abs footer"></div>
  <svg class="abs arrow" viewBox="0 0 200 200" aria-hidden="true">
    <path d="M40 190 C120 160 170 110 185 50" fill="none" stroke="var(--violet)" stroke-width="7"/>
    <polygon points="170,50 195,18 200,60" fill="var(--violet)"/>
  </svg>
  <div class="abs sponsor-tab">Corporate Sponsors</div>
  <p class="abs text limited">SPACE IS LIMITED DUE TO YACHT CAPACITY</p>
  <div class="abs prize-tab" style="top:1074px">Grand Prize</div>
  <p class="abs text prize-text" style="top:1074px">Julian Ardent Purse</p>
  <div class="abs prize-tab" style="top:1104px">Door Prize</div>
  <p class="abs text prize-text" style="top:1104px">2 Tickets to the Islander Coralwind Heritage Village</p>
  <p class="abs text extra">Other prizes for special ladies in attendance.<br>Ladies are asked to dress in <span class="script">Elegant White Ensemble</span></p>

  <div class="abs sponsor-photo">R. Lanning Photography</div>
  <div class="abs sponsor-village"><span class="mark"></span><span>Coralwind Heritage Village</span></div>
  <p class="abs text thanks">Special Thanks to our Individual Sponsors:<br>Mrs. G. Whitlow, Mr. K Prentice &amp; Mr. S. Dorsey</p>
</main>
</body>
</html>
```